Contemporary new French wine brand needs logo and series of label design

to design a new contemporary logo and series of labels for a new French wine brand. We hope to attract not just current French wine drinkers but new ones who may appreciate a less traditional and more modern style.
Updates

Reason: we are wanting to extend the project for a few days more to receive more submissions since we had fewer designs submitted than we were expecting, maybe because of the holidays.

Target Market(s)

people who follow the arts community (eg. music, theatre, visual/video arts, dance) --- all mature ages.

Industry/Entity Type

French Wine

Requirements
Must have
• a clear, memorable treatment for the name CLAVINE with accompanying logo.
Nice to have
• embossing, matte/gloss refinement, tasteful foil stamping, coated stock for the whites to help the integrity of the paper in and out of ice buckets. A combo of say, three types of fonts; a semi custom font for the brand name Clavine and maybe a script and one other.
Should not have
• not traditional French

```html
<!DOCTYPE html>
<html lang="en">
<head>
<meta charset="utf-8">
<title>Clavine — Cabernet Franc Label Series</title>
<link rel="stylesheet" href="https://fonts.googleapis.com/css2?family=Cinzel:wght@500&family=Cormorant+Garamond:wght@500&family=Pinyon+Script&display=swap">
<style>
  :root {
    --paper: #ffffff;
    --ink: #161616;
    --gold: #9a8358;
    --gold-light: #c2aa72;
    --silver: #d9d9d9;
    --onyx-top: #2c2c2c;
    --onyx-bottom: #1b1b1b;
    --band-grey: #3d3d3d;
    --band-black: #121212;
    --muted: #8a8a8a;
  }
  * { box-sizing: border-box; margin: 0; padding: 0; }
  html, body {
    width: 783px; height: 1200px; overflow: hidden;
    background: var(--paper);
  }
  .canvas {
    position: relative; width: 783px; height: 1200px;
    background: var(--paper);
  }

  /* Brand mark */
  .brand-mark {
    position: absolute; left: 50%; top: 40px;
    transform: translateX(-50%);
    width: 220px; height: 220px;
    border: 3px solid var(--ink);
    border-radius: 50%;
    display: flex; align-items: center; justify-content: center;
  }
  .brand-mark__name {
    font-family: "Cinzel", serif; font-weight: 500;
    font-size: 36px; letter-spacing: 3px; color: var(--gold);
  }

  /* Labels */
  .label-series {
    position: absolute; top: 330px; left: 0; width: 100%;
    display: flex; justify-content: center; gap: 60px;
  }
  .label {
    position: relative; width: 320px; height: 420px;
    display: flex; flex-direction: column; align-items: center;
    overflow: hidden;
  }
  .label--onyx {
    background: linear-gradient(180deg, var(--onyx-top), var(--onyx-bottom));
    --label-ink: var(--silver);
    --label-rule: #6b6b6b;
    --footer-bg: var(--band-grey);
  }
  .label--silver {
    background: linear-gradient(90deg, #8f8f8f 0%, #e6e6e6 35%, #f7f7f7 55%, #c9c9c9 80%, #9b9b9b 100%);
    --label-ink: var(--gold);
    --label-rule: var(--gold-light);
    --footer-bg: var(--band-black);
  }

  .label__wordmark {
    margin-top: 46px;
    font-family: "Cinzel", serif; font-weight: 500;
    font-size: 34px; letter-spacing: 2px; color: var(--label-ink);
  }
  .label__ornament-band {
    position: absolute; left: 0; top: 150px; width: 100%; height: 16px;
    background: linear-gradient(180deg, #0d0d0d, #262626, #0d0d0d);
  }
  .label__seal {
    position: absolute; top: 110px; left: 50%; transform: translateX(-50%);
    width: 96px; height: 96px; border-radius: 50%;
    background: var(--onyx-bottom);
    border: 1.5px solid var(--label-rule);
    display: flex; align-items: center; justify-content: center;
  }
  .label--silver .label__seal { background: #f2f2f2; }
  .label__seal-name {
    font-family: "Cinzel", serif; font-weight: 500;
    font-size: 14px; letter-spacing: 1px; color: var(--label-ink);
  }
  .label__varietal {
    position: absolute; top: 272px; width: 100%; text-align: center;
    font-family: "Cormorant Garamond", serif; font-weight: 500;
    font-size: 17px; letter-spacing: 0.5px; color: var(--label-ink);
  }
  .label__varietal span {
    display: inline-block; padding-bottom: 2px;
    border-bottom: 1px solid var(--label-rule);
  }
  .label__vintage {
    position: absolute; top: 300px; width: 100%; text-align: center;
    font-family: "Cormorant Garamond", serif; font-weight: 500;
    font-size: 16px; color: var(--label-ink);
  }
  .label__footer {
    position: absolute; left: 0; bottom: 0; width: 100%; height: 52px;
    background: var(--footer-bg);
    display: flex; align-items: center; justify-content: space-between;
    padding: 0 14px;
  }
  .label__detail {
    font-family: "Cormorant Garamond", serif; font-size: 11px;
    color: var(--muted); letter-spacing: 0.5px; width: 60px;
  }
  .label__detail--right { text-align: right; }
  .label__origin {
    font-family: "Pinyon Script", cursive; font-size: 18px; color: var(--muted);
  }
</style>
</head>
<body>
<main class="canvas">
  <div class="brand-mark">
    <span class="brand-mark__name">CLAVINE</span>
  </div>

  <section class="label-series">
    <article class="label label--onyx">
      <h1 class="label__wordmark">CLAVINE</h1>
      <div class="label__ornament-band" role="img" aria-label="Dark filigree ornament band"></div>
      <div class="label__seal"><span class="label__seal-name">CLAVINE</span></div>
      <p class="label__varietal"><span>CABERNET FRANK</span></p>
      <p class="label__vintage">2015</p>
      <footer class="label__footer">
        <span class="label__detail">750 ML</span>
        <span class="label__origin">Product of France</span>
        <span class="label__detail label__detail--right">12% ALC</span>
      </footer>
    </article>

    <article class="label label--silver">
      <h1 class="label__wordmark">CLAVINE</h1>
      <div class="label__ornament-band" role="img" aria-label="Dark filigree ornament band"></div>
      <div class="label__seal"><span class="label__seal-name">CLAVINE</span></div>
      <p class="label__varietal"><span>CABERNET FRANK</span></p>
      <p class="label__vintage">2015</p>
      <footer class="label__footer">
        <span class="label__detail">750 ML</span>
        <span class="label__origin">Product of France</span>
        <span class="label__detail label__detail--right">12% ALC</span>
      </footer>
    </article>
  </section>
</main>
</body>
</html>
```